Drug Testing & Background - Need: Our Services brochure

Seek a PDF or PPT or other file format for use as an attachments for e-mails primarily. This should also look good if it is printed on paper. Your creating a Services We Offer brochure or iPad presentation.
We would like to see designs that are super easy to read on a computer screen. It's fine to use color backgrounds and or fonts and of course related images as folks in 2016 don't really read anymore.
We are seeking something attractive to look at on a computer screen. It's fine if this is a few pages someone can quickly click through. Most important is a human can easily scan the document and 'GET' what services we provide without having to really read... So carefully choose fonts, colors and images that help in this communication.
Please also look at our current website so you can see how we present ourselves now. It's ok if you update our look and feel. We will be creating a new website so you can help us choose a new direction with this project. Building upon the puzzle peace concept you see on our current website seems right to me but your the creative person :)
2 attachments. QTR Services Overview is page 1 and the data in the PDF can be pages 2,3 as they go deeper into the services we provide.
Target Market(s)
Director or VP of Human Resources
Industry/Entity Type
Drug
Font styles to use
Look and feel

```html
<!DOCTYPE html>
<html lang="en">
<head>
<meta charset="utf-8">
<title>QTR Services Brochure</title>
<link href="https://fonts.googleapis.com/css2?family=Open+Sans:wght@300;400;600;700&family=Oswald:wght@300;400&display=swap" rel="stylesheet">
<style>
:root{
  --stage:#e9e9e9;
  --paper:#ffffff;
  --blue:#3a5f94;
  --blue-dark:#1d4f8c;
  --orange:#e8622c;
  --ink:#444a52;
  --ink-soft:#6b717a;
  --footer:#3e6496;
}
*{box-sizing:border-box;margin:0;padding:0}
html,body{width:1200px;height:523px;overflow:hidden;background:var(--stage);font-family:"Open Sans",Arial,sans-serif;color:var(--ink)}
.stage{position:relative;width:1200px;height:523px}
.page{position:absolute;top:26px;width:364px;height:470px;background:var(--paper);box-shadow:0 1px 4px rgba(0,0,0,.18);overflow:hidden}
.page-one{left:30px}.page-two{left:420px}.page-three{left:808px}
.abs{position:absolute}

.brand{display:flex;align-items:center;gap:4px}
.brand-mark{width:18px;height:18px;background:var(--blue)}
.brand-name{font-family:"Open Sans",sans-serif;font-weight:300;font-size:19px;line-height:1;color:var(--blue)}
.brand-sub{display:block;font-size:4px;font-weight:400;color:var(--ink-soft);letter-spacing:.1px;margin-top:1px}

.photo{position:absolute}

.tag{display:flex;height:14px;align-items:stretch}
.tag-icon{width:14px;background:var(--orange);display:flex;align-items:center;justify-content:center}
.tag-bar{flex:1;background:var(--blue);color:#fff;font-weight:700;font-size:6.2px;text-transform:uppercase;display:flex;align-items:center;padding-left:5px;line-height:1.05}
.tag.tall{height:20px}.tag.tall .tag-icon{width:20px}

.copy{font-size:4.1px;line-height:1.5;color:var(--ink)}
.copy p{margin-top:3px}
.copy strong{color:#2f3338}
.diamonds{list-style:none;margin-top:3px}
.diamonds li{position:relative;padding-left:6px;margin-bottom:2.5px}
.diamonds li::before{content:"";position:absolute;left:0;top:1.7px;width:2.6px;height:2.6px;background:var(--orange);transform:rotate(45deg)}
.dots{list-style:none;margin-top:3px}
.dots li{position:relative;padding-left:6px;margin-bottom:1.6px}
.dots li::before{content:"";position:absolute;left:1px;top:1.8px;width:2px;height:2px;border-radius:50%;background:var(--blue)}
.sublist{list-style:none;padding-left:2px}
.sublist li{padding-left:0;margin-bottom:0}
.sublist li::before{content:"- ";position:static;width:auto;height:auto;background:none;transform:none}

.footer{position:absolute;left:0;right:0;bottom:0;height:23px;background:var(--footer);color:#fff;font-size:4.6px;display:flex;align-items:center;justify-content:space-between;padding:0 42px 0 38px}
.footer span{display:flex;align-items:center;gap:3px}
.footer svg{width:5px;height:6px}

.hero-kicker{font-family:"Oswald",sans-serif;font-weight:400;font-size:10px;color:var(--blue-dark);letter-spacing:.2px}
.hero-title{font-family:"Oswald",sans-serif;font-weight:300;font-size:15.5px;line-height:1.05;color:var(--orange);letter-spacing:.3px;text-transform:uppercase}
.hero-sub{font-size:7.6px;font-weight:400;line-height:1.3;color:var(--ink-soft)}

.callout{font-size:10px;font-weight:300;line-height:1.4}
.callout .hl{color:var(--orange)}
.callout .lo{color:#4a4f56}

.intro{font-size:4.9px;line-height:1.5;color:var(--ink-soft)}
.service-list{list-style:none;font-size:4.9px;line-height:1.72;color:var(--ink-soft)}
.service-list li{position:relative;padding-left:5px}
.service-list li::before{content:"";position:absolute;left:0;top:3.6px;width:1.8px;height:1.8px;background:var(--orange)}
.service-list strong{color:#2f3338}
.label{font-size:5.2px;font-weight:700;color:var(--blue-dark);text-transform:uppercase;line-height:1.25}
.name-grid{display:grid;gap:4px 6px;align-items:center}
.name-grid span{font-size:5.4px;font-weight:700;color:var(--blue-dark);white-space:nowrap}
.seal{width:22px;height:22px;border-radius:50%;background:#2d4a86}
.seal.orange{background:var(--orange)}
.slab{width:40px;height:12px;background:#2d4a86}
</style>
</head>
<body>
<main class="stage">

  <section class="page page-one">
    <div class="photo" role="img" aria-label="Hands of a team fitting orange, green and blue puzzle pieces together" style="left:140px;top:0;width:224px;height:146px;background:linear-gradient(90deg,#fff 0%,rgba(226,230,236,.6) 25%,#c9d0da 55%,#b8c0cb 100%)"></div>
    <div class="abs brand" style="left:14px;top:18px">
      <span class="brand-mark"></span>
      <span class="brand-name">QTR<span class="brand-sub">Management Services, Inc.</span></span>
    </div>
    <div class="abs" style="left:14px;top:62px;width:190px">
      <div class="hero-kicker">OUR SERVICES!</div>
      <div class="hero-title">Fast, Accurate<br>&amp; Compliant...</div>
      <div class="hero-sub">Customized Domestic and Global<br>Pre-Employment Screening</div>
    </div>

    <div class="abs" style="left:14px;top:166px;width:150px">
      <div class="tag"><span class="tag-icon"><svg width="8" height="8" viewBox="0 0 8 8"><circle cx="2.5" cy="2.5" r="1.3" fill="#fff"/><circle cx="5.5" cy="2.5" r="1.3" fill="#fff"/><rect x="1" y="4.5" width="6" height="3" fill="#fff"/></svg></span><span class="tag-bar">Background Screening</span></div>
      <div class="copy">
        <p>Available in over 200 countries and territories worldwide. Services are completely customizable and dynamic to match your exact needs.</p>
        <ul class="diamonds">
          <li><strong>Social Security Number Trace</strong> - for identifying residential history, aliases, and other key data points in order to complete the most extensive background check.</li>
          <li><strong>Credit Report Checks</strong> - an indication of a candidate's integrity, stability and trustworthiness.</li>
          <li><strong>Criminal Record Checks</strong> - protects your company from the threat of negligent hiring. Driver Qualification Checks keep your drivers on the road and compliant with DOT regulations.</li>
          <li><strong>Verification and Credentialing</strong> - our specialists confirm employment, education and licensing, DOT verifications, references, transcripts and military service.</li>
          <li><strong>International Background Checks</strong> - make your international hiring more efficient with a full suite of compliant checks in more than 200 countries.</li>
        </ul>
      </div>
    </div>

    <div class="abs" style="left:190px;top:166px;width:150px">
      <div class="tag"><span class="tag-icon"><svg width="8" height="8" viewBox="0 0 8 8"><path d="M1 7 L6 2" stroke="#fff" stroke-width="1.6"/><circle cx="6.3" cy="1.7" r="1" fill="#fff"/></svg></span><span class="tag-bar">Drug Testing</span></div>
      <div class="copy">
        <p>We are your single source for all aspects of your pre-employment drug testing program. DOT and non-DOT services are managed through our system, giving you control over scheduling, exam management and compliance.</p>
        <ul class="diamonds">
          <li><strong>E-Chains</strong> - every detail of the testing process is recorded and at your fingertips.</li>
          <li><strong>Paperless &amp; Integrated</strong> - we can integrate into your current ATS, CRM or HRIS system!</li>
          <li><strong>Access</strong> - our network of certified collection sites and testing laboratories lets you build the facilities that best suit your needs.</li>
          <li><strong>Document Management</strong> - our online tools keep your program compliant with easy access to custody forms, results and records.</li>
        </ul>
      </div>
    </div>

    <div class="photo" role="img" aria-label="Business professionals seated in a bright office meeting" style="left:0;top:336px;width:178px;height:111px;background:linear-gradient(180deg,rgba(255,255,255,0) 0%,#d5dce6 30%,#a9b6c8 100%)"></div>

    <div class="abs" style="left:190px;top:300px;width:150px">
      <div class="tag"><span class="tag-icon"><svg width="8" height="8" viewBox="0 0 8 8"><circle cx="3.3" cy="3.3" r="2.2" fill="none" stroke="#fff" stroke-width="1"/><path d="M5 5 L7.3 7.3" stroke="#fff" stroke-width="1.2"/></svg></span><span class="tag-bar">DOT Screening Services</span></div>
      <div class="copy">
        <p>We perform DOT screens on your drivers, pilots and captains while complying with all Department of Transportation regulations, including DOT background checks and occupational health screening.</p>
        <ul class="diamonds">
          <li><strong>Compliance with Industry Regulations:</strong>
            <ul class="sublist">
              <li>Federal Aviation Administration (FAA).</li>
              <li>Federal Highway Administration (FHA).</li>
              <li>Federal Motor Carrier Safety Administration (FMCSA).</li>
              <li>Federal Railroad Administration (FRA).</li>
              <li>Federal Transit Administration (FTA).</li>
              <li>Pipeline and Hazardous Materials Safety Administration (PHMSA).</li>
              <li>United States Coast Guard.</li>
            </ul>
          </li>
          <li><strong>DOT Lab Based Urine Drug Testing:</strong> samples are collected at our collection sites and analyzed by a SAMHSA certified laboratory and reviewed by an MRO.</li>
        </ul>
      </div>
    </div>

    <footer class="footer">
      <span><svg viewBox="0 0 5 6"><path d="M2.5 0C1.1 0 0 1.1 0 2.4 0 4 2.5 6 2.5 6S5 4 5 2.4C5 1.1 3.9 0 2.5 0z" fill="#e8622c"/></svg>Corporate Headquarters: 1480 Harbor Point Blvd * Lake Verona, FL 33400</span>
      <span><svg viewBox="0 0 6 6"><path d="M1 0h1l.6 1.6-.8.6c.3.8.8 1.4 1.5 1.8l.7-.7L5.5 4v1C5.5 5.6 5 6 4.5 6 2 6 0 3.8 0 1.2 0 .5.4 0 1 0z" fill="#e8622c"/></svg>(800) 555 - 0148</span>
    </footer>
  </section>

  <section class="page page-two">
    <div class="photo" role="img" aria-label="Large orange puzzle piece accent" style="left:282px;top:0;width:82px;height:78px;background:linear-gradient(200deg,#e8622c 0%,#ee8352 100%)"></div>
    <div class="abs brand" style="left:18px;top:24px">
      <span class="brand-mark"></span>
      <span class="brand-name">QTR<span class="brand-sub">Management Services, Inc.</span></span>
    </div>

    <div class="abs" style="left:14px;top:66px;width:150px">
      <div class="tag tall"><span class="tag-icon"><svg width="10" height="10" viewBox="0 0 10 10"><circle cx="5" cy="5" r="3.6" fill="none" stroke="#fff" stroke-width="1"/><path d="M5 3v2.2l1.5 1" stroke="#fff" stroke-width="1" fill="none"/></svg></span><span class="tag-bar">24/7 Post-Accident Alcohol /<br>Drug Testing:</span></div>
      <div class="copy"><p>Our staff of trained collectors are prepared to assist you in a short notice at most complex post-accident scenes, whether it requires breath, urine, blood or saliva specimen collections.</p></div>
    </div>

    <div class="abs" style="left:14px;top:126px;width:150px">
      <div class="tag tall"><span class="tag-icon"><svg width="10" height="10" viewBox="0 0 10 10"><path d="M2 5a3 3 0 016 0M3.3 6a1.7 1.7 0 013.4 0M5 5v3" stroke="#fff" stroke-width=".9" fill="none"/></svg></span><span class="tag-bar">Fingerprinting Services</span></div>
      <div class="copy">
        <p>We are a leading Digital and Live Scan Fingerprinting and Level 2 Background Screening vendor. We fingerprint for the following State and Federal Agencies:</p>
        <ul class="dots">
          <li>FDLE, FBI or any registered ORI number.</li>
          <li>Agency for Healthcare Administration – (AHCA).</li>
          <li>Department of Health – (DOH).</li>
          <li>Department of Children and Families – (DCF).</li>
          <li>Agency for Persons with Disabilities – (APD).</li>
          <li>Department of Elderly Affairs – (DOEA).</li>
          <li>Florida Department of Business and Professional Regulations – (DBPR).</li>
          <li>Florida Department of Agriculture and Consumer Services – (DOACS).</li>
          <li>Florida Department of Highway Safety and Motor Vehicles – (DHSMV).</li>
          <li>Legal Name Change Fingerprinting Petitioners.</li>
          <li>Volunteer &amp; Employee Criminal History System – (VECHS).</li>
          <li>Professional and Non-Professional Guardian Programs.</li>
        </ul>
      </div>
    </div>

    <div class="photo" role="img" aria-label="Smiling professional in front of a team meeting at a conference table" style="left:170px;top:322px;width:194px;height:125px;background:linear-gradient(90deg,rgba(255,255,255,0) 0%,#e3e8ef 25%,#c3ccd9 60%,#9fb0c7 100%)"></div>

    <div class="abs" style="left:14px;top:279px;width:150px">
      <div class="tag tall"><span class="tag-icon"><svg width="10" height="10" viewBox="0 0 10 10"><rect x="2.5" y="1.5" width="5" height="7" fill="none" stroke="#fff" stroke-width=".9"/><path d="M3.7 4h2.6M3.7 5.5h2.6" stroke="#fff" stroke-width=".7"/></svg></span><span class="tag-bar">Form I-9 / E-Verify</span></div>
      <div class="copy"><p>Our paperless process will keep you totally compliant! Our system helps you with Electronic Form I-9, E-Verify, remote hires, migration and remediation of historical records, and even I-9 audits.</p></div>
    </div>

    <div class="abs" style="left:188px;top:98px;width:136px">
      <div class="tag tall"><span class="tag-icon"><svg width="10" height="10" viewBox="0 0 10 10"><path d="M5 8.5L1.5 5A2 2 0 015 2.6 2 2 0 018.5 5z" fill="#fff"/></svg></span><span class="tag-bar">Occupational Health Screening</span></div>
      <div class="copy"><p>DOT and non-DOT managed programs for pre-employment, random, post-accident, reasonable suspicion and return-to-duty needs.</p></div>
    </div>

    <div class="abs" style="left:188px;top:143px;width:136px">
      <div class="tag tall"><span class="tag-icon"><svg width="10" height="10" viewBox="0 0 10 10"><path d="M5 1.5a3.5 3.5 0 100 7 3.5 3.5 0 000-7zM5 3.3v3.4M3.3 5h3.4" stroke="#fff" stroke-width=".9" fill="none"/></svg></span><span class="tag-bar">Wellness Programs</span></div>
      <div class="copy"><p>We offer a variety of programs to keep your staff healthy on the job. From on-site flu shots to vaccination programs and physicals, we help you design and implement a solution that improves staff health and reduces long-term healthcare costs.</p></div>
    </div>

    <div class="abs" style="left:188px;top:210px;width:136px">
      <div class="tag tall"><span class="tag-icon"><svg width="10" height="10" viewBox="0 0 10 10"><path d="M2 8l4-4M6 2.2l1.8 1.8M2 2l6 6" stroke="#fff" stroke-width="1" fill="none"/></svg></span><span class="tag-bar">Other Services</span></div>
      <div class="copy">
        <ul class="dots">
          <li>Policy Creating and Regulatory Consulting.</li>
          <li>Pre-Employment DOT drug testing and DOT qualified employment questionnaires.</li>
          <li>Search of Motor Vehicle Records and CDL/S compliance.</li>
          <li>Lab Based Urine Drug Testing and Breath Alcohol Testing.</li>
          <li>Random Drug and Alcohol Testing Selection Management and Reporting.</li>
          <li>Certified results through a Medical Review Officer (MRO).</li>
        </ul>
      </div>
    </div>

    <div class="abs callout" style="left:14px;top:340px">
      <div class="hl">No Appointment</div>
      <div class="lo">Required For Office Visits.</div>
      <div class="hl" style="margin-top:6px">Onsite Fingerprinting</div>
      <div class="lo">Services Available</div>
    </div>

    <footer class="footer">
      <span><svg viewBox="0 0 5 6"><path d="M2.5 0C1.1 0 0 1.1 0 2.4 0 4 2.5 6 2.5 6S5 4 5 2.4C5 1.1 3.9 0 2.5 0z" fill="#e8622c"/></svg>Corporate Headquarters: 1480 Harbor Point Blvd * Lake Verona, FL 33400</span>
      <span><svg viewBox="0 0 6 6"><path d="M1 0h1l.6 1.6-.8.6c.3.8.8 1.4 1.5 1.8l.7-.7L5.5 4v1C5.5 5.6 5 6 4.5 6 2 6 0 3.8 0 1.2 0 .5.4 0 1 0z" fill="#e8622c"/></svg>(800) 555 - 0148</span>
    </footer>
  </section>

  <section class="page page-three">
    <div class="photo" role="img" aria-label="Businessman holding a glowing globe above a blue band with silhouettes of walking professionals" style="left:0;top:0;width:128px;height:470px;background:linear-gradient(160deg,#1d2b3d 0%,#34475e 30%,#1f6fb5 50%,#2a8ad6 62%,#1a5fa3 80%,#123d6e 100%)"></div>
    <div class="abs" style="left:0;top:296px;width:128px;text-align:center;color:#fff">
      <div style="width:26px;height:26px;background:#fff;margin:0 auto 6px"></div>
      <div style="font-weight:300;font-size:26px;line-height:1">QTR</div>
      <div style="font-size:4.6px;margin-top:2px">Management Services, Inc.</div>
    </div>

    <div class="abs brand" style="left:142px;top:18px">
      <span class="brand-mark"></span>
      <span class="brand-name">QTR<span class="brand-sub">Management Services, Inc.</span></span>
    </div>

    <p class="abs intro" style="left:142px;top:50px;width:200px">For over 30 Years, QTR Management Services has been providing Third Party Administrator (TPA) Occupational Screening Services for companies Nationwide.</p>

    <ul class="abs service-list" style="left:142px;top:84px;width:200px">
      <li>Turn-Key Drug Free Workplace Programs.</li>
      <li>Insurance Paramedical Exams.</li>
      <li>Employment Background and Credit Searches.</li>
      <li><strong>Custom API</strong> / Web Portal / Integration with your ATS or CRM Systems like Rosterly.</li>
      <li>Document and License Management and Alert System.</li>
      <li>Fingerprinting / Level II.</li>
      <li>Emergency 24/7 Onsite Collections.</li>
      <li>DNA Testing.</li>
      <li>MRO – Certified Bilingual Medical Review Officer Services.</li>
      <li>SAP – Substance Abuse Counseling.</li>
      <li>EAP – Employee Assistance Programs.</li>
      <li>Wellness Programs.</li>
      <li>Policy Development &amp; Supervisory Training.</li>
      <li>FMCSA, FRA, PHMSA, FAA, FTA, U.S. Coast Guard.</li>
    </ul>

    <div class="abs" style="left:142px;top:250px;width:212px">
      <div class="label">We are affiliates of the following laboratories</div>
      <div class="name-grid" style="grid-template-columns:repeat(5,auto);margin-top:8px;justify-content:start;gap:4px 7px">
        <span>Ternwick Labs</span><span>Bramfield Dx</span><span>Solvane</span><span>Halvern Lab</span><span>Toxora</span>
      </div>
      <div class="name-grid" style="grid-template-columns:repeat(3,auto);margin-top:9px;justify-content:start;gap:4px 14px">
        <span>Quellan Lab</span><span>Ashmore Tox</span><span>Corvex Screen</span>
      </div>
    </div>

    <div class="abs" style="left:142px;top:324px;width:212px">
      <div class="label" style="color:var(--orange)">Sample of our client's</div>
      <div class="name-grid" style="grid-template-columns:repeat(4,auto);margin-top:6px;justify-content:start;gap:4px 9px">
        <span>Fenwick Pets</span><span>Stockridge</span><span>Greywell Foods</span><span>Marlowe Supply</span>
      </div>
      <div class="name-grid" style="grid-template-columns:repeat(5,auto);margin-top:7px;justify-content:start;gap:4px 5px">
        <span>Coral Bay Transit</span><span>Orbis Imports</span><span>Verlane Univ</span><span>Ardenview</span><span>Vantrel Media</span>
      </div>
    </div>

    <div class="abs" style="left:142px;top:388px;width:100px">
      <div class="label">We are a certified<br>minority owned business</div>
      <div style="display:flex;gap:12px;margin-top:6px;padding-left:4px">
        <div class="seal orange" role="img" aria-label="Certification badge"></div>
        <div class="seal" role="img" aria-label="Certification badge"></div>
      </div>
    </div>
    <div class="abs" style="left:248px;top:388px;width:110px">
      <div class="label">Industry affiliates</div>
      <div style="display:flex;gap:5px;margin-top:6px;align-items:center">
        <div class="seal" style="width:16px;height:16px" role="img" aria-label="Affiliate badge"></div>
        <div class="slab" style="width:44px" role="img" aria-label="Affiliate badge"></div>
        <div class="seal" style="width:12px;height:12px" role="img" aria-label="Affiliate badge"></div>
      </div>
      <div style="display:flex;gap:5px;margin-top:5px;align-items:center">
        <div class="slab" style="width:26px" role="img" aria-label="Affiliate badge"></div>
        <div class="slab" style="width:48px" role="img" aria-label="Affiliate badge"></div>
      </div>
    </div>
  </section>

</main>
</body>
</html>
```